Tri-Fold Menu of Services for our Eyelash and Skin Care Spa

We need a beautiful spa service menu for our upscale spa in St. Charles Missouri. We specialize in providing treatments that are specific to the clients needs. Our services are eyelash extensions, skin care treatments, full body waxing and makeup application. Our spa colors are dark purples and greys and we are not opposed to additional colors that would complement those colors. We do a lot of eyelash extensions and while we do what those services listed we would like the skin care treatments to be in an area that would be noticed first. One of the attachments lists all of our services, descriptions and prices (please be sure to include all services and pricing. descriptions if possible). And our website has more information about us if needed. The website was not professionally done. So it DOESN'T represent our style exactly.

I HAVE ATTACHED A FEW PHOTOS BUT THEY DON'T HAVE TO BE USED.

Target Market(s)

women who would like to look their best, 35-55, annual income of 100,000+, she is usually busy and her children (if she has any) are high school age or older.

Industry/Entity Type

It Service

Font styles to use
Serif
Sans Serif

Requirements
Must have
• Must list all of our services. If it works to have the descriptions that would be great.
Nice to have
• If it works to have the descriptions of each service that would be great.

```html
<!DOCTYPE html>
<html lang="en">
<head>
<meta charset="utf-8">
<title>Velour Lash &amp; Skin Spa — Service Menu</title>
<link rel="stylesheet" href="https://fonts.googleapis.com/css2?family=Cormorant+Garamond:wght@500;600&family=Open+Sans:wght@400;600;700;800&display=swap">
<style>
  :root{
    --stage:#5d6165;
    --plum-dark:#2b1629;
    --panel:#6e6262;
    --panel-deep:#4a3c3d;
    --accent:#efb08f;
    --text:#f4efec;
    --muted:#d9cfcb;
    --rule:rgba(255,255,255,.55);
    --serif:"Cormorant Garamond", serif;
    --sans:"Open Sans", sans-serif;
  }
  *{box-sizing:border-box;margin:0;padding:0}
  html,body{width:1200px;height:800px;overflow:hidden;background:var(--stage);font-family:var(--sans);color:var(--text)}
  .brochure{position:absolute;left:40px;top:30px;width:1120px;height:740px;display:flex;background:var(--panel);box-shadow:0 10px 30px rgba(0,0,0,.35)}
  .portrait-area{position:absolute;left:0;top:0;width:746px;height:740px;
    background:radial-gradient(ellipse 230px 380px at 330px 330px,rgba(40,26,24,.85),rgba(60,44,40,.55) 55%,rgba(110,98,98,0) 80%),
               linear-gradient(180deg,var(--panel) 0%,var(--panel-deep) 100%)}
  .panel{position:relative;width:373.33px;height:740px;padding:52px 26px 20px}
  .panel::before{content:"";position:absolute;left:0;top:0;right:0;height:34px;background:var(--plum-dark);z-index:2}
  .panel + .panel{border-left:1px solid rgba(0,0,0,.18)}
  .brand{text-align:center;margin:24px 0 26px}
  .brand .rule{height:1px;background:var(--rule);width:150px;margin:0 auto}
  .brand-name{font-family:var(--serif);font-weight:600;font-size:30px;line-height:1;margin-top:14px;letter-spacing:1px}
  .brand-sub{font-size:8px;letter-spacing:1px;color:var(--muted)}
  .brand-menu{font-family:var(--serif);font-weight:600;font-size:42px;letter-spacing:3px;line-height:1;margin:2px 0 12px}
  h2{font-size:15px;font-weight:800;color:var(--accent);text-transform:uppercase;letter-spacing:.5px;margin:10px 0 3px;line-height:1}
  h2.title-case{text-transform:none;font-size:16px}
  .service{margin-bottom:9px}
  .row{display:flex;align-items:baseline;font-size:9.5px;font-weight:700;line-height:1.2}
  .row .name{white-space:nowrap}
  .row .dots{flex:1;border-bottom:1px dotted var(--rule);margin:0 4px;transform:translateY(-2px)}
  .row .price{font-weight:600;white-space:nowrap}
  .desc{font-size:8.6px;line-height:1.28;color:var(--muted);text-align:justify}
  .sub{font-size:8.6px;color:var(--muted);line-height:1.2;margin-bottom:4px}
  .compact .row{margin-bottom:1px}
  .lash-group{display:grid;grid-template-columns:90px 1fr;font-size:9.5px;font-weight:700;margin-top:3px}
  .lash-group .rows .row{font-weight:400}
  .massage-area{position:absolute;left:0;top:34px;width:100%;height:400px;
    background:linear-gradient(160deg,#6b5450 0%,#8b6a5c 45%,#5c4644 100%)}
  .panel-content{position:relative;z-index:1}
  .panel-content h2{margin-top:8px}
  .panel-content .desc{margin-top:2px}
  .eyes-area{position:absolute;left:0;bottom:0;width:100%;height:306px;
    background:linear-gradient(180deg,#c99d88 0%,#b88672 50%,#d2a892 100%)}
  .eyes-area svg{position:absolute;inset:0}
  .two-col .row .alt{margin-left:10px;font-weight:400;color:var(--muted)}
</style>
</head>
<body>
<main class="brochure">
  <div class="portrait-area" role="img" aria-label="Photo of a woman with long hair, head resting on her hand, softly lit behind the menu text"></div>

  <!-- Panel one: brand and facials -->
  <section class="panel">
    <header class="brand">
      <div class="rule"></div>
      <div class="brand-name">Velour</div>
      <div class="brand-sub">Lash &amp; Skin Spa</div>
      <div class="brand-menu">MENU</div>
      <div class="rule"></div>
    </header>

    <h2>Facial &amp; Skin Treatments</h2>
    <div class="service">
      <div class="row"><span class="name">Essential Deep Cleansing Treatment</span><span class="dots"></span><span class="price">$65 60 minutes</span></div>
      <p class="desc">This relaxing, purifying treatment consists of steaming, exfoliation and an intense deeper cleansing of clogged pores. A skin type specific ampoule is gently massaged into the skin of your face, neck and decollete, followed by a therapist selected mask. Beneficial for all skin types.</p>
    </div>
    <div class="service">
      <div class="row"><span class="name">Mini Facial</span><span class="dots"></span><span class="price">$48 30 minutes</span></div>
      <p class="desc">This express facial is ideal for those on the go. Your skin is cleansed, lightly exfoliated and gently massaged. A pore refining mask is then applied, followed by a veil of light moisturizer.</p>
    </div>
    <div class="service">
      <div class="row"><span class="name">Aromatherapy Facial</span><span class="dots"></span><span class="price">$75 60 minutes</span></div>
      <p class="desc">Our Aromatherapy facial will naturally enhance the facial benefits using fragrant oils extracted from flowers, fruits and herbs.</p>
    </div>
    <div class="service">
      <div class="row"><span class="name">Firmalux Lift &amp; Glow Treatment Facial</span><span class="dots"></span><span class="price">$95 60 minutes</span></div>
      <p class="desc">Seeking a treatment with amazing instant results? Redefining radiance and facial contouring, this exclusively formulated treatment features the latest in freeze-dried technology to deliver instant results and cumulative skin care benefits. Ideal for any skin type showing signs of aging, or as the perfect instant repair boost when you want to look your best. Proven to perform, the Solenne Firmalux Lift &amp; Glow facial renders your skin ultraluminous with a firmer, tighter and more youthfully defined appearance.</p>
    </div>
    <div class="service">
      <div class="row"><span class="name">Soothing Botanica Treatment Facial</span><span class="dots"></span><span class="price">$100 60 minutes</span></div>
      <p class="desc">This highly effective, soothing treatment calms redness and alleviates irritated or sensitive skin. A healing propolis ampoule (natural ingredient collected by bees) is applied to desensitize the skin's surface and strengthen capillaries. A cooling liftoff mask is then applied to seal in the vitamin enriched beneficial ampoule.</p>
    </div>
  </section>

  <!-- Panel two: therapies, peels, add ons, lashes -->
  <section class="panel">
    <div class="service">
      <div class="row"><span class="name">Radiance PhotoTherapy Treatment</span><span class="dots"></span><span class="price">$150 Package 8/$800</span></div>
      <p class="desc">Uses heat and light energy to gently break up areas of excess pigment while stimulating the production of new collagen. Improves skin tone, less spots, fewer pink areas, less redness, reduction in fine lines and wrinkles. Diminishes pores and restores natural radiance to your skin. Like laser treatments but unlike laser, PhotoTherapy features gentle waves of heat and light with no downtime and very little discomfort. We recommend 8 treatments, 1 to 2 times a week for best results.</p>
    </div>
    <div class="service">
      <div class="row"><span class="name">Diamond Microdermabrasion Treatment</span><span class="dots"></span><span class="price">$78</span></div>
      <p class="desc">With this treatment you will see softening of fine lines and wrinkles and smoothing of coarsely textured skin. Dull, stressed or congested skin will be brighter and clearer. The appearance of enlarged pores and acne scars will be minimized. Your at home products will be able to penetrate deeper, therefore are more effective. Or add this to any facial or most peels for just $30.</p>
    </div>

    <h2 class="title-case">Peels</h2>
    <div class="service compact">
      <div class="row"><span class="name">Acne Lift Peel</span><span class="dots"></span><span class="price">$50/1 $250/6 30 minutes</span></div>
      <p class="sub">Mild to moderate Acne peel</p>
      <div class="row"><span class="name">Lightening Lift Peel</span><span class="dots"></span><span class="price">$50/1 $250/6 30 minutes</span></div>
      <p class="sub">Pigmentation (sun/brown spots), uneven skin tone</p>
      <div class="row"><span class="name">Wrinkle Lift</span><span class="dots"></span><span class="price">$50/1 $250/6 30 minutes</span></div>
      <p class="sub">Aging, fine lines and wrinkles</p>
      <div class="row"><span class="name">Signature Lift</span><span class="dots"></span><span class="price">$100/1 $350/4 30 minutes</span></div>
      <p class="sub">Rosacea, dry/dehydrated</p>
      <div class="row"><span class="name">Perfection Lift</span><span class="dots"></span><span class="price"></span></div>
      <p class="sub">Advanced Aging, Acne, and Pigmentation (slightly more aggressive than the other options)</p>
    </div>

    <h2 class="title-case">Add Ons</h2>
    <div class="service compact">
      <div class="row"><span class="name">Microdermabrasion</span><span class="dots"></span><span class="price">$30</span></div>
      <div class="row"><span class="name">Firmalux Lift &amp; Glow Eye Treatment</span><span class="dots"></span><span class="price">$20</span></div>
      <div class="row"><span class="name">Hot or Cold Stones</span><span class="dots"></span><span class="price">$15</span></div>
      <div class="row"><span class="name">Extended Massage</span><span class="dots"></span><span class="price">$15</span></div>
      <div class="row"><span class="name">Peppermint Scalp Massage</span><span class="dots"></span><span class="price">$20</span></div>
      <div class="row"><span class="name">Foot Scrub &amp; Massage</span><span class="dots"></span><span class="price">$10</span></div>
      <div class="row"><span class="name">Aromatherapy</span><span class="dots"></span><span class="price">$15</span></div>
      <div class="row"><span class="name">Specialty Ampoule</span><span class="dots"></span><span class="price">$15</span></div>
      <div class="row"><span class="name">Specialty Mask</span><span class="dots"></span><span class="price">$13</span></div>
    </div>

    <h2>Eyelashes</h2>
    <div class="lash-group">
      <span>Classic</span>
      <div class="rows">
        <div class="row"><span class="name">Full Set</span><span class="dots"></span><span class="price">175</span></div>
        <div class="row"><span class="name">Demi Set</span><span class="dots"></span><span class="price">110</span></div>
        <div class="row"><span class="name">Touch up</span><span class="dots"></span><span class="price">60</span></div>
      </div>
    </div>
    <div class="lash-group">
      <span>Volume Technique</span>
      <div class="rows">
        <div class="row"><span class="name">Full Set</span><span class="dots"></span><span class="price">220</span></div>
        <div class="row"><span class="name">Demi Set</span><span class="dots"></span><span class="price">135</span></div>
        <div class="row"><span class="name">Touch up</span><span class="dots"></span><span class="price">72</span></div>
      </div>
    </div>
  </section>

  <!-- Panel three: waxing, tinting, massage, lash imagery -->
  <section class="panel">
    <div class="massage-area" role="img" aria-label="Photo of hands giving a relaxing face and neck massage"></div>
    <div class="panel-content">
      <h2>Waxing</h2>
      <div class="compact two-col">
        <div class="row"><span class="name">Eyebrows</span><span class="dots"></span><span class="price">$17</span></div>
        <div class="row"><span class="name">Upper Lip</span><span class="dots"></span><span class="price">$14</span></div>
        <div class="row"><span class="name">Chin</span><span class="dots"></span><span class="price">$14</span></div>
        <div class="row"><span class="name">Sides of face</span><span class="dots"></span><span class="price">$27</span></div>
        <div class="row"><span class="name">Bikini</span><span class="dots"></span><span class="price">$35</span></div>
        <div class="row"><span class="name">Brazilian</span><span class="dots"></span><span class="price">$62</span></div>
        <div class="row"><span class="name">Underarm</span><span class="dots"></span><span class="price">$20</span></div>
        <div class="row"><span class="name">Arms Full</span><span class="dots"></span><span class="price">$40 <span class="alt">Lower $30</span></span></div>
        <div class="row"><span class="name">Legs Full</span><span class="dots"></span><span class="price">$60 <span class="alt">Lower $40</span></span></div>
        <div class="row"><span class="name">Chest</span><span class="dots"></span><span class="price">$28</span></div>
        <div class="row"><span class="name">Back</span><span class="dots"></span><span class="price">$44</span></div>
      </div>

      <h2 class="title-case">Tinting</h2>
      <div class="compact">
        <div class="row"><span class="name">eyebrows</span><span class="dots"></span><span class="price">$20</span></div>
        <div class="row"><span class="name">eyelashes</span><span class="dots"></span><span class="price">$20</span></div>
        <div class="row"><span class="name">both</span><span class="dots"></span><span class="price">$30</span></div>
      </div>

      <h2>Massage</h2>
      <div class="compact">
        <div class="row"><span class="name">Neck, Back &amp; Head Massage</span><span class="dots"></span><span class="price">30 minutes $45</span></div>
        <div class="row"><span class="name">Aromatherapy Scalp Massage</span><span class="dots"></span><span class="price">10 minutes $15</span></div>
        <div class="row"><span class="name">Foot Massage and Scrub</span><span class="dots"></span><span class="price">15 minutes $20</span></div>
        <div class="row"><span class="name">Headache &amp; Migraine Relief Treatment</span><span class="dots"></span><span class="price">30 minutes $45</span></div>
        <p class="desc">Relief from headaches caused by stress, tension, hormonal imbalances or sinusitis using cold stones and massaging techniques for the face.</p>
      </div>
    </div>

    <div class="eyes-area" role="img" aria-label="Three close-up photo strips showing eyelash extensions">
      <svg width="373" height="306" viewBox="0 0 373 306" aria-hidden="true">
        <line x1="0" y1="84" x2="373" y2="64" stroke="#2b1629" stroke-width="4"/>
        <line x1="0" y1="170" x2="373" y2="144" stroke="#2b1629" stroke-width="4"/>
        <line x1="0" y1="252" x2="373" y2="222" stroke="#2b1629" stroke-width="4"/>
      </svg>
    </div>
  </section>
</main>
</body>
</html>
```